New Business Cards for Organic Meat Farm

We need a business card designed for Thornbury Farm, a meat farm in western MA. Our logo uses a hand-drawn woodcut (attached). Our color palette has been simply black and white (shown in notepad and picture of our food truck). While we are based out of western MA, we have ambitions to grow nationally, so our hope is for a classy and memorable card which will be printed on a premium quality stock from a printer like printkestrel.com.
Target Market(s)
consumers of quality meats, restauranteurs, partnering farms
Industry/Entity Type
Farming and prepared meat products
Contact Information for Business Card
Wendell Pruitt, President/Owner, wendell@thornburyfarm.com, mobile: 413-555-0172, phone: 413-555-0148, thornburyfarm.com, facebook: @thornburyfarm, instagram: @thornburyfarmma
Colors
Designer to choose colors to be used in the design.
Look and feel

```html
<!DOCTYPE html>
<html lang="en">
<head>
<meta charset="utf-8">
<title>Thornbury Farm — Business Card</title>
<link rel="stylesheet" href="https://fonts.googleapis.com/css2?family=Poppins:wght@300;400;500;600&display=swap">
<style>
  :root {
    --backdrop: #d3d7d6;
    --card: #222226;
    --ink: #ffffff;
    --ink-soft: #e6e6e6;
    --art-light: #f2f2f2;
    --art-mid: #8a8a8d;
    --rule: #8d8d90;
  }
  * { margin: 0; padding: 0; box-sizing: border-box; }
  html, body {
    width: 1200px; height: 960px; overflow: hidden;
    background: var(--backdrop);
    font-family: "Poppins", sans-serif;
    color: var(--ink);
  }
  .card {
    position: absolute;
    left: 248px;
    width: 704px; height: 402px;
    background: var(--card);
  }
  .card--front { top: 58px; }
  .card--back { top: 500px; }

  .farm-art {
    position: absolute;
    background: radial-gradient(ellipse at 50% 60%, var(--art-light) 0%, #bdbdbf 45%, var(--art-mid) 75%, rgba(34,34,38,0) 100%);
    border-radius: 50% 50% 8px 8px / 70% 70% 8px 8px;
  }
  .card--front .farm-art { left: 208px; top: 70px; width: 288px; height: 122px; }
  .card--back .farm-art { left: 51px; top: 96px; width: 229px; height: 97px; }

  .wordmark {
    position: absolute;
    font-weight: 500;
    color: var(--ink);
    text-align: center;
    white-space: nowrap;
    letter-spacing: 0.5px;
  }
  .card--front .wordmark { left: 0; width: 704px; top: 214px; font-size: 46px; }
  .card--back .wordmark { left: 20px; width: 290px; top: 214px; font-size: 34px; }

  .divider {
    position: absolute;
    left: 352px; top: 94px;
    width: 1px; height: 212px;
    background: var(--rule);
  }

  .person { position: absolute; left: 413px; top: 105px; }
  .person__name { font-size: 32px; line-height: 1; letter-spacing: 0.5px; white-space: nowrap; }
  .person__name strong { font-weight: 600; }
  .person__name span { font-weight: 300; }
  .person__role { font-size: 17px; font-weight: 400; margin-top: 8px; color: var(--ink-soft); }

  .contact { position: absolute; left: 413px; top: 190px; list-style: none; }
  .contact li {
    display: flex; align-items: center;
    height: 23px; font-size: 17px; font-weight: 400;
    white-space: nowrap;
  }
  .contact svg { width: 15px; height: 15px; margin-right: 12px; flex: none; }

  .social {
    position: absolute; left: 0; width: 704px; top: 355px;
    display: flex; justify-content: center; gap: 22px;
    font-size: 17px; font-weight: 400;
  }
  .social__item { display: flex; align-items: center; white-space: nowrap; }
  .social__dot {
    width: 14px; height: 14px; border-radius: 50%;
    background: var(--ink); margin-right: 10px;
  }
</style>
</head>
<body>

<section class="card card--front">
  <div class="farm-art" role="img" aria-label="Woodcut illustration of the farmhouse with porch and trees"></div>
  <div class="wordmark">Thornbury Farm</div>
</section>

<section class="card card--back">
  <div class="farm-art" role="img" aria-label="Woodcut illustration of the farmhouse with porch and trees"></div>
  <div class="wordmark">Thornbury Farm</div>

  <div class="divider"></div>

  <div class="person">
    <div class="person__name"><strong>Wendell</strong> <span>Pruitt</span></div>
    <div class="person__role">President/Owner</div>
  </div>

  <ul class="contact">
    <li>
      <svg viewBox="0 0 16 16" fill="none" stroke="#fff" stroke-width="1.6"><rect x="4" y="1" width="8" height="14" rx="1.5"/></svg>
      413-555-0172
    </li>
    <li>
      <svg viewBox="0 0 16 16" fill="#fff"><path d="M3.5 1.5l2.5 0 1 3.5-1.6 1.2a8 8 0 0 0 4.4 4.4L11 9l3.5 1v2.5c0 1-1 2-2 2C6.5 14.5 1.5 9.5 1.5 3.5c0-1 1-2 2-2z"/></svg>
      413-555-0148
    </li>
    <li>
      <svg viewBox="0 0 16 16" fill="none" stroke="#fff" stroke-width="1.4"><circle cx="8" cy="8" r="6.5"/><ellipse cx="8" cy="8" rx="2.8" ry="6.5"/><line x1="1.5" y1="8" x2="14.5" y2="8"/></svg>
      www.thornburyfarm.com
    </li>
    <li>
      <svg viewBox="0 0 16 16" fill="none" stroke="#fff" stroke-width="1.4"><rect x="1.5" y="4" width="13" height="9.5" rx="1"/><path d="M1.5 4.5L8 9.5l6.5-5"/></svg>
      wendell@thornburyfarm.com
    </li>
  </ul>

  <div class="social">
    <div class="social__item"><span class="social__dot"></span>@thornburyfarm</div>
    <div class="social__item"><span class="social__dot"></span>@thornburyfarmma</div>
  </div>
</section>

</body>
</html>
```